Varnok Business Card

We are a security company in Central Aus, we supply guards, patrols, alarm monitoring, cash in transit, major event security.

I would like a modern card, possibly matte finish with gloss logo.... up for anything really

Our business colors are black white and blue.

on the back side of the card i was thinking having our logo just centered or our slogan ( "Securing Your Territory 24/7" )

Industry/Entity Type

Security

Contact Information for Business Card

Company Name: Varnok Security Service
My Name: Gregor Pellham
Position: Director
Mobil: 0491 738 205
Work: 89 612 347
Fax: 89 61 23 48
Email: greg.pellham@varnok-example.com.au
web: varnok-example.com.au
Address: 14 Quarry Road Alice Springs NT 0870

```html
<!DOCTYPE html>
<html lang="en">
<head>
<meta charset="utf-8">
<title>Varnok Security Service – Business Card</title>
<link href="https://fonts.googleapis.com/css2?family=Open+Sans:wght@400;700&display=swap" rel="stylesheet">
<style>
  :root {
    --stage: #c9ccd0;
    --card-white: #f4f5f6;
    --card-shade: #e3e5e7;
    --brand-blue: #0a80c8;
    --crescent-grey: #9b9b9b;
    --text-light: #ffffff;
  }
  html, body {
    margin: 0;
    padding: 0;
    width: 1200px;
    height: 865px;
    overflow: hidden;
    background: var(--stage);
    font-family: "Open Sans", Arial, sans-serif;
  }
  .canvas {
    position: relative;
    width: 1200px;
    height: 865px;
    display: flex;
    align-items: center;
    justify-content: center;
  }
  .card {
    position: relative;
    width: 1050px;
    height: 600px;
    background: linear-gradient(135deg, var(--card-white) 0%, var(--card-shade) 100%);
    overflow: hidden;
  }
  .card-shapes {
    position: absolute;
    inset: 0;
    width: 100%;
    height: 100%;
  }
  .card-shapes .blue-field { fill: var(--brand-blue); }
  .card-shapes .grey-crescent { fill: var(--crescent-grey); }

  .brand {
    position: absolute;
    left: 95px;
    top: 245px;
    margin: 0;
    font-size: 80px;
    line-height: 1;
    font-weight: 700;
    color: var(--brand-blue);
    letter-spacing: 1px;
  }

  .contact {
    position: absolute;
    right: 40px;
    top: 50px;
    text-align: right;
    color: var(--text-light);
  }
  .contact .name {
    margin: 0;
    font-size: 30px;
    font-weight: 700;
    line-height: 1.2;
  }
  .contact .role {
    margin: 0;
    font-size: 26px;
    font-weight: 400;
    line-height: 1.2;
  }
  .contact .details {
    list-style: none;
    margin: 48px 0 0;
    padding: 0;
    font-size: 19px;
    line-height: 1.55;
  }
  .contact .details li {
    display: flex;
    justify-content: flex-end;
    align-items: center;
    gap: 8px;
    white-space: nowrap;
  }
  .contact .icon {
    width: 18px;
    height: 18px;
    fill: var(--text-light);
    flex: none;
  }
</style>
</head>
<body>
<main class="canvas">
  <section class="card" aria-label="Varnok Security Service business card">
    <svg class="card-shapes" viewBox="0 0 1050 600" preserveAspectRatio="none" aria-hidden="true">
      <path class="blue-field" d="M330,0 C560,40 640,300 520,600 L1050,600 L1050,0 Z"/>
      <path class="grey-crescent" d="M450,160 C560,280 545,460 380,600 L500,600 C590,420 580,260 450,160 Z"/>
    </svg>

    <h1 class="brand">Varnok</h1>

    <div class="contact">
      <p class="name">Gregor Pellham</p>
      <p class="role">Director</p>
      <ul class="details">
        <li>14 Quarry Road</li>
        <li>Alice Springs NT 0870</li>
        <li>0491 738 205
          <svg class="icon" viewBox="0 0 24 24" aria-label="phone"><path d="M6.6 10.8a15.1 15.1 0 0 0 6.6 6.6l2.2-2.2a1 1 0 0 1 1-.25 11.4 11.4 0 0 0 3.6.57 1 1 0 0 1 1 1V20a1 1 0 0 1-1 1A17 17 0 0 1 3 4a1 1 0 0 1 1-1h3.5a1 1 0 0 1 1 1c0 1.250.2 2.45.57 3.57a1 1 0 0 1-.25 1z"/></svg>
        </li>
        <li>89 61 23 48
          <svg class="icon" viewBox="0 0 24 24" aria-label="fax"><path d="M7 2h8l3 3v5h2a2 2 0 0 1 2 2v8a2 2 0 0 1-2 2H4a2 2 0 0 1-2-2v-8a2 2 0 0 1 2-2h3zm2 2v6h7V6h-3V4zM5 13v2h3v-2zm5 0v2h3v-2zm5 0v2h3v-2zM5 17v2h3v-2zm5 0v2h3v-2zm5 0v2h3v-2z"/></svg>
        </li>
        <li>greg.pellham@varnok-example.com.au
          <svg class="icon" viewBox="0 0 24 24" aria-label="email"><path d="M2 5h20v14H2zm2 2v.5l8 5 8-5V7zm0 2.9V17h16V9.9l-8 5z"/></svg>
        </li>
        <li>varnok-example.com.au</li>
      </ul>
    </div>
  </section>
</main>
</body>
</html>
```